We need your help in designing the graphical look of the home page of our web site: Quellnest.com.

Quellnest is an FREE online service that brings consumers and service providers together through online reservations.

Our service is in fact a web application (similar to brindlo calendar), so we will be using forms, widgets, menus and standard web controls (buttons, fields, links, etc). We need a design that will be easy to integrate with our programming.

This design project is for the HOME page, but we will choose the designer that will design the web page in photoshop in layers, so we can easily derive our other secondary pages ourselves.

If you have any questions please send us a message and we will gladly update the brief with a response.

Happy Designing!
Updates

Hi all, the menu on the home page should be something standard, like: Pricing, features, how it works.

once a user is logged in, they will see their toolbox at all times:
- My Nest (links to their main page of bookings)
- My Faborites (view favorite businesses and book quickly with them)
- Settings (set parameters of their account)

There should be a My Profile page as well. 

Thanks!

Reason: I have extended the deadline to receive more designs.

Hi All,

UPDATE: we changed our vision of the home page to have a much simpler design.  something along the lines of tumbrella vexnor and mor tan.

HOME PAGE:
light colors with white background.  simple, simple, simple!

header should not be big, logo, change language link. try with search bar (what and where).

body should be simple, with an image + register form only.

footer with links to pages for more info:
- Privacy,
- Getting started
- How it works
- Contact us
- FAQ
- Pricing

LOGGED IN PAGE:
when logged in, the header can be the same or reduced to maximize the "working area" (body).
body can be a 2 or 3 column design, as we have a main working area.  in your design, show a calendar.  we need a toolbar (side or top) that will have these buttons, links: MyNest, My Favorites, Settings, My Profile.
We need a section that will display latest messages or notifications.
keep the footer with the links.

Thank you all.

Reason: Holidays

Reason: holidays... lets spend time with our families!

Target Market(s)

Young and mobile consumers + professionals, businesses, restaurants and commerces wishing to offer online reservations (appointments and reservations)

Industry/Entity Type

Brindlo

Requirements
Must have
• - Easy to integrate with web programming
- light weight visual design. We want something with light tone colors as background
- home page will have a content slider that will show some catch phrases.
- Overall design should be more on the "cartoony" side. Should give a casual, humour and friendly ambiance.

The home page should have these sections:
- a search section for consumers to find local businesses. They will search by specifying "What?" & "Where?"
- a content slider that will cycle through catch phrases and features. Each pane should have an image representative of the text.
- have 4 highlighted sections
- QuellNest is great for (list of different businesses types that use quelnest)
- QuellNest is available for FREE to everyone
- Main features list (accept 24/7 reservations, never reveal your schedule, automatic reminders, marketing campaigns)
- The more you quell, the more you save! (info on our loyalty program that entitles consumers to greater savings and benefits).

One a user logs in, all the certer page info will be replaced by a content div that will allow content to display based on selected menu item
- My Nest (opens the main section where all happens. This section should have a design that gives the impression that we're looking in a box)
- My Profile
- My Favorites
Should not have
• - Don't use actual photos of real people, rather opt for sketches and cartoony characters.

```html
<!DOCTYPE html>
<html lang="en">
<head>
<meta charset="utf-8">
<title>QuellNest – Online Reservation</title>
<link href="https://fonts.googleapis.com/css2?family=Arimo:wght@400;700&display=swap" rel="stylesheet">
<style>
  :root{
    --page:#ffffff;
    --stage-top:#eaf5f6;
    --stage-low:#dcecee;
    --footer:#c3dde0;
    --band-a:#2aa3c0;
    --band-b:#1787a4;
    --ink-title:#4a6f8a;
    --ink-soft:#86acc4;
    --ink-link:#3f6e8c;
    --ink-follow:#34607e;
    --accent:#2fb0e0;
    --logo-disc:#2b2523;
    --icon-disc:#c2dfe4;
    --icon-ink:#3a3a3a;
    --field-line:#b9c4c6;
    --field-fill:#f3f5f5;
    --green-a:#dff25c;
    --green-b:#a8d018;
    --tan-a:#ece1ad;
    --tan-b:#c6b26d;
  }
  *{box-sizing:border-box;margin:0;padding:0}
  html,body{width:1200px;height:770px;overflow:hidden;background:var(--page)}
  body{position:relative;font-family:"Arimo",Arial,sans-serif}
  .stage{position:absolute;left:0;top:0}
  .abs{position:absolute}

  .brand-disc{left:198px;top:130px;width:164px;height:164px;border-radius:50%;background:var(--logo-disc);
    display:flex;align-items:center;justify-content:center}
  .brand-name{color:var(--accent);font-weight:700;font-size:22px}

  .intro-title{left:395px;top:152px;font-size:23px;font-weight:700;color:var(--ink-title)}
  .intro-text{left:396px;top:188px;width:400px;font-size:16px;line-height:27px;color:var(--ink-soft)}
  .feature-icons{left:392px;top:256px;display:flex;gap:15px}
  .feature-icon{width:41px;height:41px;border-radius:50%;background:var(--icon-disc);
    box-shadow:inset 0 0 0 1px #b0d2d8;display:flex;align-items:center;justify-content:center}

  .register-card{left:811px;top:26px;width:275px;height:328px;background:#fff;border:3px solid #bfd8db;
    border-radius:11px;box-shadow:0 3px 6px rgba(80,120,130,.25);padding:0 20px 0 20px}
  .register-title{margin-top:33px;font-size:21px;font-weight:700;color:var(--accent)}
  .rule{height:1px;background:#d4dcdd;margin-top:12px}
  .register-note{margin-top:12px;font-size:11px;color:#62a7c6}
  .field{display:block;width:230px;height:27px;margin-top:13px;border:1px solid var(--field-line);
    background:var(--field-fill);box-shadow:inset 0 1px 2px rgba(0,0,0,.12);font:15px "Arimo",Arial,sans-serif;
    color:#555;padding:4px 11px}
  .register-note + .field{margin-top:6px}
  .btn-join{display:block;margin-top:14px;width:109px;height:34px;border-radius:6px;border:1px solid #98bb1a;
    background:linear-gradient(var(--green-a),var(--green-b));font:700 15px "Arimo",Arial,sans-serif;color:#2b2b1a}
  .register-foot{margin-top:17px;font-size:12px;color:#3b5d77;padding-top:12px;border-top:1px solid #d4dcdd}
  .register-foot a{color:var(--accent);margin-left:8px}

  .search-lead{left:148px;top:410px;font-size:18px;font-weight:700;color:#fff}
  .search-label{font-size:11px;font-weight:700;color:#e8f6fa}
  .search-field{display:block;margin-top:5px;height:25px;border:1px solid #8fbfcc;background:#f5f8f8;
    font:13px "Arimo",Arial,sans-serif;color:#444;padding:4px 8px}
  .btn-search{left:870px;top:404px;width:91px;height:27px;border-radius:4px;border:1px solid #a8955a;
    background:linear-gradient(var(--tan-a),var(--tan-b));font:15px "Arimo",Arial,sans-serif;color:#2e2e2e}

  .lang{left:47px;top:527px;width:88px;height:24px;border:1px solid #a9c0c3;border-radius:3px;background:#f4f7f7;
    font-size:14px;color:#3a4d58;padding:3px 9px}
  .lang svg{position:absolute;right:8px;top:9px}
  .footer-links{left:157px;top:530px;display:flex;font-size:14px;color:var(--ink-link)}
  .footer-links a{color:inherit;text-decoration:none;padding:0 9px;border-left:1px solid #a7c6cb}
  .footer-links a:first-child{padding-left:0;border-left:0}
  .follow{right:38px;top:526px;display:flex;align-items:center;gap:6px}
  .follow-label{font-size:17px;font-weight:700;color:var(--ink-follow);margin-right:4px}
  .social{height:27px;padding:0 7px;border:1px solid #7d9ea8;border-radius:3px;background:#f3f7f8;
    font-size:12px;color:var(--ink-follow);display:flex;align-items:center;text-decoration:none}
</style>
</head>
<body>
  <svg class="stage" width="1200" height="770" viewBox="0 0 1200 770" aria-hidden="true">
    <defs>
      <linearGradient id="bandFill" x1="0" y1="0" x2="0" y2="1">
        <stop offset="0" stop-color="#2aa3c0"/><stop offset="1" stop-color="#1787a4"/>
      </linearGradient>
      <linearGradient id="upperFill" x1="0" y1="0" x2="0" y2="1">
        <stop offset="0" stop-color="#e6f3f4"/><stop offset="1" stop-color="#f0f8f8"/>
      </linearGradient>
    </defs>
    <polygon points="202,74 1086,74 1120,381 85,381" fill="url(#upperFill)"/>
    <polygon points="85,381 1120,381 1145,446 59,446" fill="url(#bandFill)"/>
    <polygon points="59,446 1145,446 1172,514 34,514" fill="#dcecee"/>
    <rect x="34" y="514" width="1138" height="256" fill="#c3dde0"/>
  </svg>

  <div class="abs brand-disc" role="img" aria-label="QuellNest logo"><span class="brand-name">QuellNest</span></div>

  <h1 class="abs intro-title">Online Reservation</h1>
  <p class="abs intro-text">Mattis, risus aliquam cum a, pulvinar platea pulvinar risus pulvinar odio lundium dis nec sagittis eu mid</p>

  <div class="abs feature-icons">
    <span class="feature-icon"><svg width="22" height="22" viewBox="0 0 22 22"><path d="M8 3v11.5a3.5 3 0 1 0 2 2.7V8l8-2v7a3.5 3 0 1 0 2 2.7V1z" fill="#3a3a3a"/></svg></span>
    <span class="feature-icon"><svg width="22" height="24" viewBox="0 0 22 24"><circle cx="11" cy="9" r="7" fill="#3a3a3a"/><rect x="8" y="15" width="6" height="5" fill="#3a3a3a"/><rect x="9" y="21" width="4" height="2" fill="#3a3a3a"/></svg></span>
    <span class="feature-icon"><svg width="22" height="24" viewBox="0 0 22 24"><text x="11" y="20" text-anchor="middle" font-family="Arimo,Arial,sans-serif" font-weight="700" font-size="22" fill="#3a3a3a">$</text></svg></span>
    <span class="feature-icon"><svg width="24" height="24" viewBox="0 0 24 24"><path d="M21 3c-1-1-3 0-4 1l-4 4-9-2-2 2 7 4-3 4-3-1-1 1 3 2 2 3 1-1-1-3 4-3 4 7 2-2-2-9 4-4c1-1 2-3 1-4z" fill="#3a3a3a"/></svg></span>
    <span class="feature-icon"><svg width="24" height="24" viewBox="0 0 24 24"><circle cx="12" cy="12" r="10" fill="#3a3a3a"/><path d="M12 12V5M12 12l5 3" stroke="#c2dfe4" stroke-width="2" fill="none"/></svg></span>
  </div>

  <form class="abs register-card">
    <h2 class="register-title">Register</h2>
    <div class="rule"></div>
    <p class="register-note">QuellNest is available for FREE to everyone</p>
    <input class="field" type="text" placeholder="Your Name">
    <input class="field" type="email" placeholder="Email">
    <input class="field" type="password" placeholder="Password">
    <button class="btn-join" type="button">Join Now !</button>
    <p class="register-foot">Already a QuellNest member?<a href="#">Sign In »</a></p>
  </form>

  <p class="abs search-lead">Make a FREE reservation</p>
  <label class="abs" style="left:389px;top:389px"><span class="search-label">What</span>
    <input class="search-field" style="width:227px" type="text" placeholder="e.g. Italian food, XXXX film"></label>
  <label class="abs" style="left:631px;top:389px"><span class="search-label">Where</span>
    <input class="search-field" style="width:228px" type="text" placeholder="e.g. Some Neighborhood"></label>
  <button class="abs btn-search" type="button">Search</button>

  <div class="abs lang">English<svg width="10" height="6" viewBox="0 0 10 6"><path d="M0 0h10L5 6z" fill="#55646c"/></svg></div>
  <nav class="abs footer-links">
    <a href="#">Privacy</a><a href="#">Getting Started</a><a href="#">How It Works</a><a href="#">Contact Us</a><a href="#">FAQ</a><a href="#">Pricing</a>
  </nav>
  <div class="abs follow">
    <span class="follow-label">Follow Us:</span>
    <a class="social" href="#">Tumbrella</a>
    <a class="social" href="#">Vexnor</a>
    <a class="social" href="#">Brindlo</a>
    <a class="social" href="#">Feed</a>
  </div>
</body>
</html>
```